Carrow Building Partners Website

Need a dynamic corporate website that can be built on with time. We want to get our information out to the world and have a place where customers can submit requests for proposals.

Target Market(s)

Custom home owners and buyers. Architects and Real Estate Agents.

Industry/Entity Type

Construction

Number of Pages Required

3 page

Font styles to use
Serif
Sans Serif

Requirements
Must have
• Company logo, about, company contact information, biography, contact, projects,
• Sleek, modern, clean, attractive design.
• Online form customers can use for filling out a request for project proposal.
• Linkedin hyperlink.
• Uses www.carrowbuildingpartners.com

```html
<!DOCTYPE html>
<html lang="en">
<head>
<meta charset="utf-8">
<title>Carrow Building Partners</title>
<link href="https://fonts.googleapis.com/css2?family=Open+Sans:wght@400;600;700;800&display=swap" rel="stylesheet">
<style>
:root{
  --blue:#1d4f9c;
  --blue-dark:#163d7a;
  --ink:#333;
  --muted:#777;
  --dark:#1e1e1e;
  --darker:#151515;
  --light:#f1f1f1;
  --line:#d6d6d6;
  --white:#fff;
}
*{margin:0;padding:0;box-sizing:border-box}
html,body{width:1200px;height:3276px;overflow:hidden}
body{font-family:"Open Sans",Arial,sans-serif;color:var(--ink);background:var(--white);position:relative}
.abs{position:absolute}
/* header */
.site-header{position:absolute;top:0;left:0;width:1200px;height:72px;background:var(--white);border-bottom:1px solid #e5e5e5}
.brand{position:absolute;left:22px;top:18px;display:flex;align-items:center;gap:10px}
.brand-mark{width:34px;height:34px;background:var(--blue)}
.brand-name{font-size:17px;font-weight:700;color:var(--blue);letter-spacing:.5px;line-height:1.1;width:170px}
.main-nav{position:absolute;right:40px;top:0;display:flex;gap:34px;height:72px;align-items:center}
.main-nav a{font-size:12px;font-weight:600;color:#555;text-decoration:none;text-transform:uppercase;padding:6px 0}
.main-nav a.active{color:var(--blue);border-bottom:2px solid var(--blue)}
/* hero */
.hero{position:absolute;top:72px;left:0;width:1200px;height:520px;background:linear-gradient(160deg,#9fb3c4 0%,#6d7f8f 40%,#4f5963 70%,#33383e 100%)}
.hero-caption{position:absolute;top:170px;left:0;width:1200px;text-align:center;color:var(--white)}
.hero-caption h1{font-size:46px;font-weight:800;letter-spacing:1px}
.hero-caption p{width:560px;margin:14px auto 0;font-size:14px;line-height:1.5}
.btn-ghost{display:inline-block;margin-top:18px;padding:6px 18px;font-size:11px;font-weight:700;border:1px solid var(--white);color:var(--white);background:rgba(0,0,0,.35)}
.hero-arrow{position:absolute;top:240px}
.cta-bar{position:absolute;top:592px;left:0;width:1200px;height:60px;background:var(--blue);color:var(--white)}
.cta-bar p{position:absolute;left:130px;top:20px;font-size:13px}
.btn-light{position:absolute;right:130px;top:16px;padding:6px 16px;background:var(--white);color:var(--blue);font-size:11px;font-weight:700}
/* welcome */
.section-title{font-size:24px;font-weight:700;text-align:center;color:#2a2a2a;text-transform:none}
.section-title span{color:var(--blue)}
.welcome{position:absolute;top:652px;left:0;width:1200px;height:340px}
.welcome .section-title{position:absolute;top:38px;width:1200px}
.welcome-text{position:absolute;left:130px;top:110px;width:720px;font-size:13px;line-height:1.75;color:#555}
.welcome-text p+p{margin-top:16px}
.welcome-photo{position:absolute;left:890px;top:108px;width:170px;height:122px;background:linear-gradient(180deg,#8fb3d6,#4d7fa8 55%,#6b8c5c)}
/* offer */
.offer{position:absolute;top:992px;left:0;width:1200px;height:480px}
.offer .section-title{position:absolute;top:28px;width:1200px;text-transform:uppercase}
.offer-sub{position:absolute;top:68px;width:1200px;text-align:center;font-size:11px;color:var(--muted);line-height:1.5}
.service{position:absolute;width:420px;display:flex;gap:18px}
.service-icon{flex:none;width:52px;height:52px;border-radius:50%;background:var(--blue);display:flex;align-items:center;justify-content:center}
.service h3{font-size:18px;font-weight:700;color:var(--blue);margin-top:4px}
.service p{font-size:11px;color:var(--muted);line-height:1.5;margin-top:4px}
/* projects */
.projects{position:absolute;top:1472px;left:0;width:1200px;height:870px;background:var(--dark)}
.projects .section-title{position:absolute;top:52px;width:1200px;color:var(--white);text-transform:uppercase}
.filters{position:absolute;left:130px;top:120px;display:flex;gap:18px;font-size:12px;color:#bbb}
.filters .on{color:var(--white);font-weight:700}
.tile{position:absolute;width:300px;height:320px}
.tile-overlay{position:absolute;inset:0;background:rgba(0,0,0,.45);color:var(--white)}
.tile-overlay .icons{position:absolute;top:110px;left:0;width:300px;display:flex;justify-content:center;gap:12px}
.tile-overlay .icons span{width:38px;height:38px;border-radius:50%;background:var(--blue);display:flex;align-items:center;justify-content:center}
.tile-overlay h4{position:absolute;top:180px;left:38px;font-size:20px;font-weight:700}
.tile-overlay p{position:absolute;top:210px;left:38px;font-size:11px}
/* contact */
.contact{position:absolute;top:2342px;left:0;width:1200px;height:418px;background:var(--light)}
.contact .section-title{position:absolute;top:36px;width:1200px;text-transform:uppercase}
.rfp-form{position:absolute;left:130px;top:118px;width:500px}
.field-row{display:flex;gap:20px;margin-bottom:12px}
.field{flex:1;height:32px;border:1px solid var(--line);background:var(--white);font-size:12px;color:#999;padding:7px 10px}
.field.message{height:110px}
.btn-submit{display:inline-block;margin-top:6px;padding:8px 20px;background:var(--blue);color:var(--white);font-size:11px;font-weight:700}
.contact-info{position:absolute;left:660px;top:112px;width:410px}
.contact-info h3{font-size:16px;font-weight:700;color:var(--blue)}
.contact-info p{font-size:12px;line-height:1.65;color:#555;margin-top:8px}
.contact-lines{display:flex;gap:40px;margin-top:22px;font-size:12px;color:#444}
.contact-lines div{display:flex;align-items:center;gap:8px}
/* clients */
.clients{position:absolute;top:2760px;left:0;width:1200px;height:192px}
.clients h2{position:absolute;left:130px;top:18px;font-size:24px;font-weight:700;color:#2a2a2a;text-transform:uppercase}
.clients h2 span{color:var(--blue)}
.clients h2::after{content:"";display:block;width:60px;height:3px;background:var(--blue);margin-top:6px}
.client-row{position:absolute;left:60px;top:100px;width:1080px;display:flex;align-items:center;justify-content:space-between}
.client-arrow{width:32px;height:32px;background:var(--blue);display:flex;align-items:center;justify-content:center}
.client-badge{width:130px;height:64px;border:1px solid var(--line);display:flex;align-items:center;justify-content:center}
/* footer */
.site-footer{position:absolute;top:2952px;left:0;width:1200px;height:324px;background:var(--dark);color:#bbb}
.foot-col{position:absolute;top:40px;font-size:11px;line-height:1.7}
.foot-col h4{font-size:15px;color:var(--white);font-weight:700;margin-bottom:12px}
.foot-col ul{list-style:none}
.social{display:flex;gap:8px;margin-top:14px}
.social span{width:22px;height:22px;border-radius:50%;background:#3a6fc4}
.newsletter-field{margin-top:14px;display:flex}
.newsletter-field span{width:170px;height:28px;background:var(--white);color:#999;font-size:11px;padding:6px 8px}
.newsletter-field b{width:32px;height:28px;background:var(--blue)}
.copyright{position:absolute;bottom:0;left:0;width:1200px;height:36px;background:var(--darker);text-align:center;font-size:11px;line-height:36px;color:#999}
</style>
</head>
<body>

<header class="site-header">
  <div class="brand"><span class="brand-mark"></span><span class="brand-name">CARROW BUILDING PARTNERS</span></div>
  <nav class="main-nav">
    <a class="active">Home</a><a>About</a><a>Services</a><a>Projects</a><a>Blog</a><a>Contact</a>
  </nav>
</header>

<section class="hero" role="img" aria-label="Photo of a construction worker holding a yellow hard hat with a building site behind">
  <svg class="hero-arrow" style="left:22px" width="20" height="36" viewBox="0 0 20 36"><path d="M16 4 4 18l12 14" fill="none" stroke="#fff" stroke-width="4"/></svg>
  <svg class="hero-arrow" style="right:22px" width="20" height="36" viewBox="0 0 20 36"><path d="M4 4l12 14L4 32" fill="none" stroke="#fff" stroke-width="4"/></svg>
  <div class="hero-caption">
    <h1>WE BUILD YOUR DREAMWORLD</h1>
    <p>Lorem Ipsum is simply dummy text of the printing and typesetting industry. Lorem Ipsum has been the industry's standard dummy text ever since the 1500s.</p>
    <span class="btn-ghost">READ MORE</span>
  </div>
</section>

<div class="cta-bar">
  <p>Looking for a quality constructor for your next project?</p>
  <span class="btn-light">GET A QUOTE</span>
</div>

<section class="welcome">
  <h2 class="section-title">Welcome to <span>Carrow Building Partners</span></h2>
  <div class="welcome-text">
    <p>Lorem Ipsum is simply dummy text of the printing and typesetting industry. Lorem Ipsum has been the industry's standard dummy text ever since the 1500s, when an unknown printer took a galley of type and scrambled it to make a type specimen book. It has survived not only five centuries, but also the leap into electronic typesetting, remaining essentially unchanged. It was popularised in the 1960s with the release of Letraset sheets containing Lorem Ipsum passages, and more recently with desktop publishing software.</p>
    <p>Lorem Ipsum is simply dummy text of the printing and typesetting industry. Lorem Ipsum has been the industry's standard dummy text ever since the 1500s, when an unknown printer took a galley of type and scrambled it to make a type specimen book of the printing and typesetting industry.</p>
  </div>
  <div class="welcome-photo" role="img" aria-label="Photo of a modern glass office building"></div>
</section>

<section class="offer">
  <h2 class="section-title">What we <span>offer</span></h2>
  <p class="offer-sub">Lorem Ipsum is simply dummy text of the printing and typesetting industry.<br>Lorem Ipsum has been the industry's standard dummy text.</p>

  <div class="service" style="left:180px;top:130px">
    <div class="service-icon"><svg width="26" height="26" viewBox="0 0 26 26"><circle cx="13" cy="13" r="10" fill="none" stroke="#fff" stroke-width="2"/><path d="M3 13h20M13 3c4 4 4 16 0 20M13 3c-4 4-4 16 0 20" fill="none" stroke="#fff" stroke-width="1.6"/></svg></div>
    <div><h3>LOREM IPSUM</h3><p>Lorem Ipsum is simply dummy text of the printing and typesetting industry. Lorem Ipsum has been the</p></div>
  </div>
  <div class="service" style="left:660px;top:130px">
    <div class="service-icon"><svg width="26" height="26" viewBox="0 0 26 26"><path d="M13 22 4 13a5 5 0 0 1 9-6 5 5 0 0 1 9 6z" fill="#fff"/></svg></div>
    <div><h3>LOREM IPSUM</h3><p>Lorem Ipsum is simply dummy text of the printing and typesetting industry. Lorem Ipsum has been the</p></div>
  </div>
  <div class="service" style="left:180px;top:230px">
    <div class="service-icon"><svg width="26" height="26" viewBox="0 0 26 26"><path d="M13 4a9 9 0 1 1-8 5M5 4v5h5" fill="none" stroke="#fff" stroke-width="2.4"/></svg></div>
    <div><h3>LOREM IPSUM</h3><p>Lorem Ipsum is simply dummy text of the printing and typesetting industry. Lorem Ipsum has been the</p></div>
  </div>
  <div class="service" style="left:660px;top:230px">
    <div class="service-icon"><svg width="26" height="26" viewBox="0 0 26 26"><path d="M5 21 17 9M19 4l3 3-4 4-3-3zM5 5l16 16" fill="none" stroke="#fff" stroke-width="2.6"/></svg></div>
    <div><h3>LOREM IPSUM</h3><p>Lorem Ipsum is simply dummy text of the printing and typesetting industry. Lorem Ipsum has been the</p></div>
  </div>
  <div class="service" style="left:180px;top:330px">
    <div class="service-icon"><svg width="26" height="26" viewBox="0 0 26 26"><circle cx="8" cy="13" r="4" fill="none" stroke="#fff" stroke-width="2.4"/><circle cx="18" cy="13" r="4" fill="none" stroke="#fff" stroke-width="2.4"/></svg></div>
    <div><h3>LOREM IPSUM</h3><p>Lorem Ipsum is simply dummy text of the printing and typesetting industry. Lorem Ipsum has been the</p></div>
  </div>
  <div class="service" style="left:660px;top:330px">
    <div class="service-icon"><svg width="26" height="26" viewBox="0 0 26 26"><path d="M3 10 13 4l10 6zM5 11h16v2H5zM6 14h2v6H6zM12 14h2v6h-2zM18 14h2v6h-2zM4 21h18v2H4z" fill="#fff"/></svg></div>
    <div><h3>LOREM IPSUM</h3><p>Lorem Ipsum is simply dummy text of the printing and typesetting industry. Lorem Ipsum has been the</p></div>
  </div>
</section>

<section class="projects">
  <h2 class="section-title">Recent projects</h2>
  <div class="filters"><span class="on">All</span><span>Architecture</span><span>Buildings</span><span>Office</span><span>Interior Design</span></div>

  <div class="tile" style="left:0;top:168px;background:linear-gradient(160deg,#7e8a94,#3f4a52)" role="img" aria-label="Photo of an engineer reviewing plans on a site">
    <div class="tile-overlay">
      <div class="icons">
        <span><svg width="16" height="16" viewBox="0 0 16 16"><circle cx="7" cy="7" r="4.5" fill="none" stroke="#fff" stroke-width="2"/><path d="M10 10l4 4" stroke="#fff" stroke-width="2"/></svg></span>
        <span><svg width="16" height="16" viewBox="0 0 16 16"><path d="M6 10l4-4M5 8 3 10a2.5 2.5 0 0 0 3.5 3.5L8 12M11 8l2-2a2.5 2.5 0 0 0-3.5-3.5L8 4" fill="none" stroke="#fff" stroke-width="1.8"/></svg></span>
      </div>
      <h4>Lorem Ipsum</h4>
      <p>It is a long established fact that a reader</p>
    </div>
  </div>
  <div class="tile" style="left:300px;top:168px;background:linear-gradient(180deg,#9ab0c6,#d8dde2 55%,#7a7f84)" role="img" aria-label="Photo of a modern white villa"></div>
  <div class="tile" style="left:600px;top:168px;background:linear-gradient(180deg,#b9c7d4,#5d6a76 60%,#3a3f44)" role="img" aria-label="Photo of a contemporary house at dusk"></div>
  <div class="tile" style="left:900px;top:168px;background:linear-gradient(180deg,#a7c2dd,#c9a98a 55%,#8c7664)" role="img" aria-label="Photo of an apartment tower against blue sky"></div>
  <div class="tile" style="left:0;top:498px;background:linear-gradient(180deg,#cfd5da,#9fa7ad 50%,#6f7a82)" role="img" aria-label="Photo of a concrete modern residence"></div>
  <div class="tile" style="left:300px;top:498px;background:linear-gradient(180deg,#9bb4c9,#e0e2e0 50%,#6c7b5e)" role="img" aria-label="Photo of a two storey family home with garden"></div>
  <div class="tile" style="left:600px;top:498px;background:linear-gradient(180deg,#bfcfdf,#8e9297 55%,#565b60)" role="img" aria-label="Photo of a modern residential building"></div>
  <div class="tile" style="left:900px;top:498px;background:linear-gradient(180deg,#8fb0d0,#a3704e 55%,#5d4432)" role="img" aria-label="Photo of a brick apartment block"></div>
</section>

<section class="contact">
  <h2 class="section-title">Get in <span>touch</span></h2>
  <div class="rfp-form">
    <div class="field-row"><span class="field">Name</span><span class="field">Phone</span></div>
    <div class="field-row"><span class="field">Email</span></div>
    <div class="field-row"><span class="field message">Message</span></div>
    <span class="btn-submit">SUBMIT</span>
  </div>
  <div class="contact-info">
    <h3>CONTACT US NOW</h3>
    <p>Lorem Ipsum is simply dummy text of the printing and typesetting industry. Lorem Ipsum has been the industry's standard dummy text ever since the 1500s, when an unknown printer took a galley of type and scrambled it to make a type specimen book. It has survived not only five centuries, but also the leap into electronic typesetting, remaining essentially unchanged. It was popularised in the 1960s with the release of Letraset sheets containing.</p>
    <div class="contact-lines">
      <div><svg width="22" height="22" viewBox="0 0 22 22"><circle cx="11" cy="11" r="11" fill="#1d4f9c"/><path d="M7 6h3l1 3-2 1a7 7 0 0 0 3 3l1-2 3 1v3c-5 1-10-4-9-9z" fill="#fff"/></svg>555-012-4321</div>
      <div><svg width="22" height="22" viewBox="0 0 22 22"><circle cx="11" cy="11" r="11" fill="#1d4f9c"/><path d="M5 7h12v8H5zM5 7l6 5 6-5" fill="none" stroke="#fff" stroke-width="1.4"/></svg>info@carrowbuildingpartners.com</div>
    </div>
  </div>
</section>

<section class="clients">
  <h2>Our <span>Clintes</span></h2>
  <div class="client-row">
    <span class="client-arrow"><svg width="12" height="14" viewBox="0 0 12 14"><path d="M9 2 3 7l6 5" fill="none" stroke="#fff" stroke-width="2.4"/></svg></span>
    <span class="client-badge"><svg width="30" height="30"><rect x="5" y="5" width="20" height="20" fill="#444"/></svg></span>
    <span class="client-badge"><svg width="30" height="30"><rect x="5" y="5" width="20" height="20" fill="none" stroke="#444" stroke-width="3"/></svg></span>
    <span class="client-badge"><svg width="30" height="30"><circle cx="15" cy="15" r="11" fill="none" stroke="#444" stroke-width="3"/></svg></span>
    <span class="client-badge"><svg width="30" height="30"><circle cx="15" cy="15" r="10" fill="#444"/></svg></span>
    <span class="client-badge"><svg width="30" height="30"><rect x="6" y="6" width="18" height="18" fill="#666"/></svg></span>
    <span class="client-badge"><svg width="30" height="30"><circle cx="15" cy="15" r="11" fill="#666"/></svg></span>
    <span class="client-arrow"><svg width="12" height="14" viewBox="0 0 12 14"><path d="M3 2l6 5-6 5" fill="none" stroke="#fff" stroke-width="2.4"/></svg></span>
  </div>
</section>

<footer class="site-footer">
  <div class="foot-col" style="left:130px;width:230px">
    <h4>About Company</h4>
    <p>Lorem Ipsum is simply dummy text of the printing and typesetting industry. Lorem Ipsum has been the industry's standard dummy text ever since the 1500s, when an unknown printer took a galley of type and scrambled it.</p>
    <div class="social"><span></span><span></span><span></span><span></span></div>
  </div>
  <div class="foot-col" style="left:420px;width:220px">
    <h4>E-NEWSLETTER</h4>
    <p>Subscribe to our newsletter to receive project news and updates.</p>
    <div class="newsletter-field"><span>Your email</span><b></b></div>
  </div>
  <div class="foot-col" style="left:700px;width:140px">
    <h4>Navigation</h4>
    <ul><li>› Home</li><li>› About</li><li>› Services</li><li>› Projects</li><li>› Blog</li><li>› Contact</li></ul>
  </div>
  <div class="foot-col" style="left:880px;width:200px">
    <h4>Company Info</h4>
    <p>1420 Harbor Lane, Suite 8, Millbrook</p>
    <p>(555) 014-2290</p>
    <p>info@carrowbuildingpartners.com</p>
    <p>www.carrowbuildingpartners.com</p>
  </div>
  <div class="copyright">Copyright © Carrow Building Partners site 2016. All Rights Reserved</div>
</footer>

</body>
</html>
```